Web Design

We are Carvento’s new and used car supermarket, we need a clean and nice look web design.

What included on homepage:
1. Logo
2. Slideshow (additional)
3. Menu - Home, About us, New cars, Used cars, Contact us
4. Advance Search
5. Customer Reviews
6. Social links - facebook, twitter , youtube
7. Banner Ads
8. Recent News
9. Newsletter

We just need psd files, home and contact us.

Industry/Entity Type

Used Car

Number of Pages Required

2 page

Requirements
Must have
• Webpage are well designed and in accordance with the color of the logo that is displayed in the file attachment.

```html
<!DOCTYPE html>
<html lang="en">
<head>
<meta charset="utf-8">
<title>Carvento Car Supermarket</title>
<link href="https://fonts.googleapis.com/css2?family=Roboto:wght@400;500;700&family=Roboto+Condensed:wght@400;700&display=swap" rel="stylesheet">
<style>
:root{
  --blue:#2d7fc1;
  --blue-light:#4e9bd6;
  --heading:#3b8fcf;
  --red:#e2404c;
  --text:#333;
  --muted:#666;
  --line:#cfcfcf;
  --footer:#5c5c5c;
  --footer-dark:#3b3b3b;
  --bg:#fff;
}
*{margin:0;padding:0;box-sizing:border-box}
html,body{width:820px;height:1200px;overflow:hidden;background:var(--bg);font-family:"Roboto",Arial,sans-serif;color:var(--text)}
.page{position:relative;width:820px;height:1200px;border-top:5px solid #222}
.abs{position:absolute}
.brand{left:117px;top:22px;font-family:"Roboto",sans-serif;font-weight:500;color:var(--blue);line-height:1}
.brand-name{display:block;font-size:24px;letter-spacing:.5px}
.brand-sub{display:block;font-size:9px;letter-spacing:2.5px;margin-top:3px}
.nav{left:319px;top:33px;display:flex;gap:18px;font-size:9px;color:#555}
.nav .active{color:var(--red)}
.social{left:621px;top:25px;display:flex;gap:6px}
.social span{width:23px;height:23px;border-radius:50%;display:block;border:2px solid #ddd}
.hero{left:117px;top:69px;width:586px;height:245px;border:2px solid #e3e3e3;box-shadow:0 6px 8px rgba(0,0,0,.15)}
.hero-photo{position:absolute;inset:0;background:linear-gradient(135deg,#9aa3aa 0%,#c9cdd0 30%,#b3262f 55%,#3c3f44 80%,#2a2b2e 100%)}
.hero-arrows{position:absolute;left:17px;top:189px;display:flex;gap:3px}
.hero-arrows span{width:22px;height:22px;background:#111;color:#fff;font-size:14px;display:flex;align-items:center;justify-content:center}
.hero-title{position:absolute;left:84px;top:190px;color:#fff;font-family:"Roboto Condensed",sans-serif;font-weight:700;font-size:19px;text-shadow:0 1px 3px #000}
.search{position:absolute;right:2px;top:20px;width:168px;height:200px;background:rgba(64,140,200,.92);padding:9px 12px}
.search h3{color:#fff;font-weight:400;font-size:12px;text-align:center;margin-bottom:10px}
.select{height:21px;background:#fff;margin-bottom:13px;font-size:7px;color:#555;display:flex;align-items:center;padding-left:6px;position:relative}
.select::after{content:"";position:absolute;right:0;top:0;width:20px;height:21px;border-left:1px solid #ccc;background:linear-gradient(#fff,#e6e6e6)}
.price{color:#fff;font-size:7px;margin-top:-4px}
.slider{height:4px;background:#1f3d57;border-radius:2px;margin:7px 0 18px;position:relative}
.slider i{position:absolute;top:-3px;width:5px;height:10px;background:#ddd}
.btn-search{display:block;margin:0 auto;width:63px;height:20px;background:var(--red);color:#fff;font-size:8px;text-align:center;line-height:20px;border-radius:2px}
.section-title{color:var(--heading);font-size:12px;font-weight:400}
.rule{height:1px;background:var(--line)}
.card{width:146px;height:127px;border:1px solid #ddd;padding:3px}
.card .photo{height:91px}
.card .model{font-family:"Roboto Condensed",sans-serif;color:var(--red);font-size:7px;margin-top:4px}
.card .quote{font-family:"Roboto Condensed",sans-serif;font-size:8px;color:#333;margin-top:3px}
.card .detail{position:absolute;right:3px;bottom:7px;width:47px;height:16px;background:var(--blue-light);color:#fff;font-size:7px;font-weight:700;text-align:center;line-height:16px;border-radius:2px}
.ad{left:584px;top:356px;width:119px;height:198px;background:var(--blue-light)}
.ad-art{height:108px;background:linear-gradient(#e8782e,#f0a15a)}
.ad p{color:#fff;text-align:center;font-family:"Roboto Condensed",sans-serif}
.news-item{font-size:6.5px;color:#555;line-height:9.6px;border-bottom:1px solid var(--line);padding-bottom:7px;margin-bottom:6px}
.news-item b{color:var(--red);font-weight:400;display:block}
.review{display:flex;gap:10px;width:290px}
.review .avatar{width:82px;height:68px;flex:none;box-shadow:0 2px 3px rgba(0,0,0,.3)}
.review h4{color:var(--red);font-weight:400;font-size:9px;margin-bottom:5px}
.review p{font-size:7.5px;color:#555;line-height:15px;width:178px}
.stars{display:flex;gap:1px;margin-top:3px}
.stars i{width:7px;height:7px;background:#e8603a}
.stars i.off{background:#bbb}
.brands{left:115px;top:938px;width:586px;height:61px;background:#f1f1f1;display:flex;align-items:center;justify-content:space-around;font-family:"Roboto Condensed",sans-serif;font-size:10px;color:#555}
.footer{left:0;top:1019px;width:820px;height:113px;background:var(--footer);color:#fff}
.fcol{position:absolute;top:23px}
.fcol h5{font-weight:400;font-size:10px;padding-bottom:4px;border-bottom:1px solid #888;margin-bottom:10px;width:76px}
.fcol li{list-style:none;font-size:6.5px;line-height:13px}
.news-form{display:flex;margin-top:6px}
.news-form span{width:101px;height:20px;background:#fff;color:#999;font-size:6px;line-height:20px;padding-left:8px}
.news-form b{width:27px;height:20px;background:var(--red);font-size:7px;line-height:20px;text-align:center}
.bottom{left:0;top:1132px;width:820px;height:68px;background:var(--footer-dark);color:#fff}
.bottom .links{position:absolute;left:120px;top:18px;font-size:9px;letter-spacing:.3px}
.bottom .copy{position:absolute;left:119px;top:37px;font-size:7.5px}
.bottom .icons{position:absolute;left:597px;top:20px;display:flex;gap:4px}
.bottom .icons span{width:18px;height:18px;border-radius:50%;background:#eee}
</style>
</head>
<body>
<div class="page">
  <div class="abs brand"><span class="brand-name">CARVENTO'S</span><span class="brand-sub">CAR SUPERMARKET</span></div>
  <nav class="abs nav"><span class="active">HOME</span><span>ABOUT US</span><span>NEW CARS</span><span>USED CARS</span><span>CONTACT US</span></nav>
  <div class="abs social" aria-label="Social links">
    <span style="background:#3b5a9a"></span><span style="background:#2aa5dd"></span><span style="background:#d8322c"></span>
  </div>

  <section class="abs hero">
    <div class="hero-photo" role="img" aria-label="Red hatchback car photographed in a city street"></div>
    <div class="hero-arrows"><span>&#8249;</span><span>&#8250;</span></div>
    <div class="hero-title">WE WILL BUY YOUR CAR!</div>
    <form class="search">
      <h3>ADVANCE SEARCH</h3>
      <div class="select">ALL CAR TYPES</div>
      <div class="select">ALL CAR BRANDS</div>
      <div class="select">ALLCAR MODELS</div>
      <div class="price">PRICE FILTER</div>
      <div class="slider"><i style="left:30px"></i><i style="left:110px"></i></div>
      <span class="btn-search">SEARCH</span>
    </form>
  </section>

  <h2 class="abs section-title" style="left:116px;top:337px">FEATURED VEHICLES ON SALE</h2>
  <div class="abs rule" style="left:116px;top:356px;width:460px"></div>

  <div class="abs card" style="left:117px;top:363px"><div class="photo" role="img" aria-label="Yellow hatchback" style="background:linear-gradient(135deg,#8fb6d6,#e2a024 50%,#6b6b6b)"></div><div class="model">RIDGEWAY TOURER</div><div class="quote">REQUEST A FREE QUOTE</div><span class="detail">DETAILE</span></div>
  <div class="abs card" style="left:270px;top:363px"><div class="photo" role="img" aria-label="Red minivan in the city" style="background:linear-gradient(135deg,#9a9a9a,#b8252e 55%,#555)"></div><div class="model">RIDGEWAY TOURER</div><div class="quote">REQUEST A FREE QUOTE</div><span class="detail">DETAILE</span></div>
  <div class="abs card" style="left:427px;top:364px"><div class="photo" role="img" aria-label="Dark grey SUV" style="background:linear-gradient(135deg,#777,#3c3e42 55%,#999)"></div><div class="model">RIDGEWAY TOURER</div><div class="quote">REQUEST A FREE QUOTE</div><span class="detail">DETAILE</span></div>

  <div class="abs card" style="left:117px;top:502px"><div class="photo" role="img" aria-label="Olive compact SUV" style="background:linear-gradient(135deg,#444,#6f6a55 50%,#a87a3a)"></div><div class="model">RIDGEWAY TOURER</div><div class="quote">REQUEST A FREE QUOTE</div><span class="detail">DETAILE</span></div>
  <div class="abs card" style="left:270px;top:502px"><div class="photo" role="img" aria-label="Silver SUV on a coastal road" style="background:linear-gradient(135deg,#9fb0b8,#c7c9c8 50%,#6c6e6c)"></div><div class="model">RIDGEWAY TOURER</div><div class="quote">REQUEST A FREE QUOTE</div><span class="detail">DETAILE</span></div>
  <div class="abs card" style="left:427px;top:503px"><div class="photo" role="img" aria-label="Black SUV at dusk" style="background:linear-gradient(135deg,#5a6f86,#222 55%,#3d3d3d)"></div><div class="model">RIDGEWAY TOURER</div><div class="quote">REQUEST A FREE QUOTE</div><span class="detail">DETAILE</span></div>

  <div class="abs card" style="left:117px;top:638px"><div class="photo" role="img" aria-label="Grey sedan in motion" style="background:linear-gradient(135deg,#5f6a4e,#8a8f86 50%,#4d5257)"></div><div class="model">RIDGEWAY TOURER</div><div class="quote">REQUEST A FREE QUOTE</div><span class="detail">DETAILE</span></div>
  <div class="abs card" style="left:270px;top:638px"><div class="photo" role="img" aria-label="Silver SUV on a mountain road" style="background:linear-gradient(135deg,#6b7784,#b9b3a5 50%,#6e4d3a)"></div><div class="model">RIDGEWAY TOURER</div><div class="quote">REQUEST A FREE QUOTE</div><span class="detail">DETAILE</span></div>
  <div class="abs card" style="left:427px;top:639px"><div class="photo" role="img" aria-label="Red crossover in the city" style="background:linear-gradient(135deg,#9a9a9a,#c8242e 55%,#444)"></div><div class="model">RIDGEWAY TOURER</div><div class="quote">REQUEST A FREE QUOTE</div><span class="detail">DETAILE</span></div>

  <aside class="abs ad">
    <div class="ad-art" role="img" aria-label="Cartoon orange car illustration"></div>
    <p style="font-size:12px;margin-top:14px">WE WILL BUY</p>
    <p style="font-size:12px;margin-top:7px">YOUR CAR!</p>
    <p style="font-size:7px;margin-top:10px;font-weight:700">WHAT'S YOUR CAR WORTH?</p>
  </aside>

  <h2 class="abs section-title" style="left:586px;top:572px;font-size:11px">RECENT NEWS</h2>
  <svg class="abs" style="left:684px;top:568px" width="18" height="18" viewBox="0 0 18 18" aria-label="RSS feed"><rect width="18" height="18" rx="3" fill="#f28a28"/><circle cx="5" cy="13" r="1.8" fill="#fff"/><path d="M4 8a6 6 0 0 1 6 6M4 4a10 10 0 0 1 10 10" stroke="#fff" stroke-width="2" fill="none"/></svg>
  <div class="abs rule" style="left:584px;top:589px;width:118px"></div>
  <div class="abs" style="left:584px;top:595px;width:118px">
    <div class="news-item"><b>April 15, 2015</b>Mes cuml dia. Sted in lacus uterto enim asci aliiqt sit amet.</div>
    <div class="news-item"><b>April 16, 2015</b>Mes cuml dia. Sted in lacus uterto enim asci aliiqt sit amet.</div>
    <div class="news-item"><b>April 17, 2015</b>Mes cuml dia. Sted in lacus uterto enim asci aliiqt sit amet.</div>
    <div class="news-item" style="border:none"><b>April 18, 2015</b>Mes cuml dia. Sted in lacus uterto enim asci aliiqt sit amet.</div>
    <div style="font-size:6.5px;color:var(--heading);font-style:italic;margin-top:-3px">SEE MORE</div>
  </div>

  <h2 class="abs section-title" style="left:122px;top:781px">CUSTOMER REVIEWS</h2>
  <div class="abs" style="left:689px;top:776px;font-size:14px">&#8249; &#8250;</div>
  <div class="abs rule" style="left:116px;top:800px;width:586px"></div>
  <div class="abs review" style="left:126px;top:812px">
    <div class="avatar" role="img" aria-label="Customer portrait" style="background:linear-gradient(135deg,#d9d4cf,#8a5a3c)"></div>
    <div><h4>IPSUM IS SIMPLY DUMMY TEXT</h4><p>Lorem Ipsum has been the industry's standard dummy text ever since &nbsp;the 1500s, when an</p><div class="stars"><i></i><i></i><i></i><i></i><i class="off"></i></div></div>
  </div>
  <div class="abs review" style="left:424px;top:812px">
    <div class="avatar" role="img" aria-label="Customer portrait" style="background:linear-gradient(135deg,#e8e4df,#c9a57a)"></div>
    <div><h4>IPSUM IS SIMPLY DUMMY TEXT</h4><p>Lorem Ipsum has been the industry's standard dummy text ever since &nbsp;the 1500s, when an</p><div class="stars"><i></i><i></i><i></i><i></i><i class="off"></i></div></div>
  </div>
  <div class="abs rule" style="left:116px;top:896px;width:586px"></div>

  <h2 class="abs section-title" style="left:115px;top:910px">OUR POPULAR BRANDS</h2>
  <div class="abs brands">
    <span>Velocca</span><span>Arlen</span><span>Bavor</span><span>Nordvik</span><span>Velocca</span><span>Steinmark</span><span>Hoshiro</span><span>Lioncourt</span>
  </div>

  <footer class="abs footer">
    <div class="fcol" style="left:117px"><h5>How We Help</h5><ul><li>Lead Generation</li><li>Tactics Management</li><li>Start-Up Website</li><li>Website Facelifts</li></ul></div>
    <div class="fcol" style="left:263px"><h5>Services</h5><ul><li>Social Media Coaching</li><li>Website Analysis</li><li>Framewise Website Design</li><li>Newsletters</li></ul></div>
    <div class="fcol" style="left:423px"><h5>Results</h5><ul><li>Testimonials</li><li>Companies</li><li>Contractors &amp; Construction</li><li>Manufacturing</li></ul></div>
    <div class="fcol" style="left:576px"><h5 style="width:127px">Newsletter</h5><p style="font-size:6.5px;line-height:13px;width:130px">Lorem Ipsum has been the industry's standard dummy text ever since</p><div class="news-form"><span>mail@example.com</span><b>JOIN</b></div></div>
  </footer>
  <div class="abs bottom">
    <div class="links">About us &nbsp;| &nbsp;Terms of use &nbsp;| &nbsp;Privacy policy &nbsp;| &nbsp;Copyright &nbsp;| &nbsp;Contact</div>
    <div class="copy">Copy Right © 2014. All rights reserved.</div>
    <div class="icons" aria-label="Social links"><span></span><span></span><span></span><span></span><span></span></div>
  </div>
</div>
</body>
</html>
```